Brightwire Hollow Business cards

one side I would like my logo (uploaded) and the other side I want my details. I'm an electrician in sydney. The logo side I'm happy with just a white background and our logo in the middle.

Details for other side
24/7 Sydney Electrician
Marcus Pell
0431 587 219
marcus@brightwirehollow.com.au
brightwirehollow.com.au
icons for facebook, instagram, linked in

Industry/Entity Type

electrician

Contact Information for Business Card

company info

```html
<!DOCTYPE html>
<html lang="en">
<head>
<meta charset="utf-8">
<title>Brightwire Hollow – Business Cards</title>
<link rel="stylesheet" href="https://fonts.googleapis.com/css2?family=Rubik:wght@400;500;700&display=swap">
<style>
  :root {
    --stage: #d6d6d6;
    --card-white: #ffffff;
    --brand-red: #e91e27;
    --back-red: #ee3526;
    --ink: #111111;
    --cream: #f8e2cf;
  }
  * { box-sizing: border-box; margin: 0; padding: 0; }
  html, body {
    width: 1200px; height: 780px; overflow: hidden;
    background: var(--stage);
    font-family: "Rubik", Arial, sans-serif;
  }
  .canvas { position: relative; width: 1200px; height: 780px; }

  .card {
    position: absolute; top: 220px;
    width: 550px; height: 336px;
    overflow: hidden;
    box-shadow: 0 12px 30px rgba(0,0,0,0.25);
  }
  .card--details { left: 35px; background: var(--card-white); }
  .card--brand { left: 615px; background: var(--back-red); }

  .card__swoosh { position: absolute; inset: 0; width: 100%; height: 100%; }

  .wordmark {
    position: absolute; left: 0; right: 0;
    text-align: center; font-weight: 700; line-height: 1;
  }
  .card--details .wordmark {
    top: 38px; font-size: 34px; color: var(--brand-red); letter-spacing: 0.5px;
  }
  .card--brand .wordmark {
    top: 138px; font-size: 52px; color: var(--cream); letter-spacing: 1px;
  }

  .contact {
    position: absolute; left: 150px; top: 92px; width: 300px;
    text-align: center; color: var(--ink);
  }
  .contact__name { font-size: 30px; font-weight: 700; color: var(--brand-red); line-height: 1.05; }
  .contact__role { font-size: 15px; font-weight: 500; margin-top: 2px; }
  .contact__rule { width: 120px; height: 1px; background: var(--ink); margin: 6px auto 6px; }
  .contact__icons { display: flex; justify-content: center; gap: 8px; margin-bottom: 4px; }
  .contact__icons svg { width: 13px; height: 13px; }
  .contact__line { font-size: 14px; font-weight: 500; line-height: 1.35; }
  .contact__phone { font-size: 16px; font-weight: 700; }
  .social { display: flex; justify-content: center; gap: 10px; margin-top: 8px; }
  .social span { width: 15px; height: 15px; border-radius: 50%; background: var(--brand-red); }

  .tagline {
    position: absolute; left: 40px; bottom: 24px;
    color: var(--card-white); font-weight: 700; font-size: 15px;
    letter-spacing: 0.5px; text-transform: uppercase;
  }
</style>
</head>
<body>
<main class="canvas">

  <section class="card card--details">
    <svg class="card__swoosh" viewBox="0 0 550 336" preserveAspectRatio="none" aria-hidden="true">
      <path d="M0,175 Q250,330 550,298 L550,336 L0,336 Z" fill="var(--brand-red)"/>
      <path d="M30,180 Q270,320 530,294 Q270,310 30,180 Z" fill="var(--ink)" stroke="var(--ink)" stroke-width="2"/>
    </svg>

    <div class="wordmark">Brightwire Hollow</div>

    <div class="contact">
      <div class="contact__name">Marcus Pell</div>
      <div class="contact__role">Electrician</div>
      <div class="contact__rule"></div>
      <div class="contact__icons">
        <svg viewBox="0 0 16 16" aria-label="phone"><path d="M4 1l2.5 3-1.5 1.5c.8 2 2.5 3.7 4.5 4.5L11 8.5l3 2.5-1.5 3C7 13.5 2.5 9 2 3z" fill="var(--brand-red)"/></svg>
        <svg viewBox="0 0 16 16" aria-label="email"><rect x="1" y="3" width="14" height="10" fill="var(--brand-red)"/><path d="M1 3l7 6 7-6" fill="none" stroke="#fff" stroke-width="1.2"/></svg>
        <svg viewBox="0 0 16 16" aria-label="website"><circle cx="8" cy="8" r="7" fill="var(--brand-red)"/><path d="M1 8h14M8 1v14M8 1c-3 3-3 11 0 14M8 1c3 3 3 11 0 14" fill="none" stroke="#fff" stroke-width="1"/></svg>
      </div>
      <div class="contact__line contact__phone">0431 587 219</div>
      <div class="contact__line">marcus@brightwirehollow.com.au</div>
      <div class="contact__line">www.brightwirehollow.com.au</div>
      <div class="social" aria-label="social media links"><span></span><span></span><span></span></div>
    </div>

    <div class="tagline">24/7 Sydney Electrician</div>
  </section>

  <section class="card card--brand">
    <div class="wordmark">Brightwire Hollow</div>
  </section>

</main>
</body>
</html>
```